Training Manual

We need a black/white InDesign template created for our training manual. We're looking to slightly modernize the design and make it as visually appealing as possible while also remaining highly-readable and not tiring to look at at for long periods of time.
A sample chapter from our current manual is attached. - The manual overall consists of 260 pages, there are a few diagrams but the manual consists primarily of text.
Training

```html
<!DOCTYPE html>
<html lang="en">
<head>
<meta charset="utf-8">
<title>Chapter 5: The Devotional Life</title>
<link href="https://fonts.googleapis.com/css2?family=Mulish:ital,wght@0,400;0,600;0,700;1,400;1,700&display=swap" rel="stylesheet">
<style>
  :root {
    --ink: #1a1a1a;
    --quote: #3a3a3a;
    --brand: #c9c9c9;
    --footer-dark: #2a2a2a;
    --footer-light: #ffffff;
    --paper: #ffffff;
  }
  * { box-sizing: border-box; margin: 0; padding: 0; }
  html, body { width: 848px; height: 1200px; overflow: hidden; background: var(--paper); }
  body { font-family: "Mulish", sans-serif; color: var(--ink); position: relative; }

  .brand {
    position: absolute; left: 36px; top: 40px;
    display: flex; align-items: center; gap: 8px;
    font-size: 28px; font-weight: 400; letter-spacing: 1px; color: var(--brand);
  }
  .brand-dot { width: 12px; height: 12px; border-radius: 50%; background: var(--brand); }

  .section-title {
    position: absolute; left: 61px; top: 118px;
    font-size: 17.5px; font-weight: 700;
    border-bottom: 1px solid var(--ink); padding-bottom: 1px;
  }
  .section-title .numeral { display: inline-block; width: 32px; }

  .content { position: absolute; left: 92px; top: 150px; width: 690px; font-size: 14.2px; line-height: 19px; }
  .point { display: flex; margin-bottom: 10px; }
  .point-label { width: 26px; flex: none; }
  .items { list-style: none; margin-left: 27px; }
  .item { display: flex; margin-bottom: 19px; }
  .item-num { width: 23px; flex: none; }
  .item-body { flex: 1; }
  .item-body p { margin-bottom: 8px; }
  .quote { color: var(--quote); }
  .quote strong { font-weight: 700; font-style: italic; color: var(--ink); }
  .cite { text-decoration: underline; font-style: italic; }

  .footer {
    position: absolute; left: 0; top: 1149px; width: 848px; height: 23px;
    background: linear-gradient(90deg, var(--footer-dark) 0%, #6e6e6e 35%, #bdbdbd 70%, var(--footer-light) 100%);
    display: flex; align-items: center; justify-content: space-between;
    padding: 0 47px 0 53px; font-size: 14.5px; font-weight: 700;
  }
  .page-number { color: #ffffff; }
  .chapter-name { color: var(--ink); }
</style>
</head>
<body>
  <div class="brand"><span class="brand-dot"></span>LUMEN</div>

  <h2 class="section-title"><span class="numeral">II.</span>Personal Prayer – The Key to Spiritual Power</h2>

  <div class="content">
    <div class="point"><span class="point-label">A.</span><span>Prayer is the secret to Spiritual power.</span></div>
    <ol class="items">
      <li class="item"><span class="item-num">1.</span><div class="item-body">
        <p>Prayer is essential to spiritual life and all spiritual activity. Just as we must have air to breathe in order to stay alive, so we must engage in prayer in order to have spiritual life.</p>
        <p class="quote">Prayer is the breath of the soul. – <span class="cite">Field Servants, p. 254.</span></p>
        <p class="quote">The darkness of the evil one encloses those who neglect to pray. – <span class="cite">Ibid., p. 94.</span></p>
      </div></li>
      <li class="item"><span class="item-num">2.</span><div class="item-body">
        <p>Without prayer, our religious experience degenerates into a mere outward form, much like the “dry bones” that had the word preached to them, but had not yet received the breath of life (Ezek. 37:7-8). This was the condition of the church in the Teacher’s day; they searched the Scriptures for information rather than a real relationship with God. The Teacher commended their study of the Bible, but added “You are not willing to come to Me that you may have life” (Jn. 5:39-40).</p>
        <p class="quote">[Prayer] is <strong>the secret of spiritual power. No other means of grace can be substituted,</strong> and the health of the soul be preserved. Prayer brings the heart into immediate contact with the Well-spring of life, and strengthens the sinew and muscle of the religious experience. Neglect the exercise of prayer, or engage in prayer spasmodically, now and then, as seems convenient, and you lose your hold on God. The spiritual faculties lose their vitality, the religious experience lacks health and vigor. – <span class="cite">Field Servants, p. 254.</span></p>
      </div></li>
      <li class="item"><span class="item-num">3.</span><div class="item-body">
        <p>This is why we are encouraged to “pray without ceasing” (1 Thes. 5:17). This does not mean to engage in long, drawn-out, formal praying, but to be in an attitude of open communion with God, kind of like being on the phone with someone and not hanging up.</p>
        <p class="quote">The Master commands, “Pray without ceasing;” that is, <strong>keep the mind uplifted to God,</strong> the source of all power and efficiency. – <span class="cite">Letters to Leaders, p. 510</span>.</p>
        <p class="quote">Unceasing prayer is the <strong>unbroken union</strong> of the soul with God… - <span class="cite">Paths to Peace, p. 97.</span></p>
        <p class="quote">Pray in your closet, and as you go about your daily labor <strong>let your heart be often uplifted to God.</strong> It was <strong>thus</strong> that <strong>the faithful elder walked with God.</strong> – <span class="cite">Ibid., pp. 98-99.</span></p>
        <p class="quote"><strong>Cultivate the habit of talking with the Saviour</strong> when you are alone, when you are walking, and when you are busy with your daily labor. Let the heart be <strong>continually uplifted</strong> in silent petition for help, for light, for strength, for knowledge. Let every breath be a prayer. – Quiet Hours, p. 179.</p>
        <p class="quote">Daily prayer is as <strong>essential</strong> to growth in grace, and even to spiritual life itself, as is temporal food to physical well-being. We should <strong>accustom ourselves</strong> to often lift the thoughts to God in prayer. <strong>If the mind wanders, we must bring it back;</strong> by persevering effort, habit will finally make it easy. We cannot for one moment separate ourselves from the Master with safety. We may have His presence to attend us at every step, but only by observing the conditions which He has Himself laid down. – <span class="cite">Daily Mercies, p. 289.</span></p>
      </div></li>
    </ol>
  </div>

  <footer class="footer">
    <span class="page-number">2</span>
    <span class="chapter-name">Chapter 5: The Devotional Life</span>
  </footer>
</body>
</html>
```